VELARDO Tribute to the Prince of Samba Lenta

11” x 17” 4-color poster design, press-ready. We will be using a US-based online printer, QuillPrint.

You have worked with my father Howard (Hal) Penwick before and the Lark Hollow Stage Foundantion. This poster design need is for an upcoming event

Provided is a link to a Google Drive Folder with ideas to inspire the poster design. However, all ideas are welcome. Addittionally, the names and photos of the featured performers are OPTIONAL to include in the design.

Link to Shared Drive: https://files.brindlecove.net/folders/7qz-4k81XTRWPLMenbcaAvgDoRsYJKf?usp=share_link

They are:
Gus Pemberly, Music Director
Neil Soward, Emcee
Ida Lusk, Vocalist

And a cast of professional musicians.

Event Time and Location:

Sunday, May 17⋅3:00 – 5:00pm
Lark Hollow Auditorium
2716 W 8th Ct, Tulsa, OK 74125, USA

All Seats Reserved
Tickets Available at LarkHollowStage.com

```html
<!DOCTYPE html>
<html lang="en">
<head>
<meta charset="utf-8">
<title>VELARDO – Tribute to the Prince of Samba Lenta</title>
<link href="https://fonts.googleapis.com/css2?family=Oswald:wght@400;500;600;700&family=Open+Sans:wght@400;600;700&display=swap" rel="stylesheet">
<style>
  :root {
    --paper: #ece5d6;
    --paper-deep: #ddd3bf;
    --ink: #3a3632;
    --ink-soft: #5c554d;
    --ink-faint: #a89d8a;
    --photo-dark: #4a4640;
    --photo-light: #b8afa0;
  }
  html, body {
    margin: 0;
    padding: 0;
    overflow: hidden;
    background: var(--paper);
  }
  .poster {
    position: relative;
    width: 849px;
    height: 1200px;
    overflow: hidden;
    background: radial-gradient(ellipse at 50% 35%, #f2ece0 0%, var(--paper) 55%, var(--paper-deep) 100%);
    font-family: "Open Sans", Arial, sans-serif;
    color: var(--ink);
  }
  .backdrop-texture {
    position: absolute;
    left: 0; top: 0;
    width: 849px; height: 1200px;
    background: linear-gradient(160deg, rgba(200,190,170,0.25), rgba(236,229,214,0) 60%);
  }
  .event-title {
    position: absolute;
    left: 34px;
    top: 78px;
    margin: 0;
    font-family: "Oswald", Impact, sans-serif;
    font-weight: 700;
    font-size: 150px;
    line-height: 1;
    letter-spacing: -2px;
    color: var(--ink);
  }
  .hero-portrait {
    position: absolute;
    left: 600px;
    top: 60px;
    width: 215px;
    height: 300px;
    background: linear-gradient(200deg, var(--photo-light) 0%, var(--photo-dark) 70%, rgba(74,70,64,0) 100%);
    border-radius: 6px 6px 40px 40px;
    opacity: 0.85;
  }
  .tagline {
    position: absolute;
    left: 0; right: 0;
    top: 318px;
    margin: 0;
    text-align: center;
    font-family: "Oswald", Impact, sans-serif;
    font-weight: 600;
    font-size: 28px;
    letter-spacing: 1px;
    color: var(--ink);
  }
  .description {
    position: absolute;
    left: 150px;
    width: 560px;
    top: 420px;
    margin: 0;
    font-size: 13.5px;
    line-height: 1.45;
    text-align: left;
    color: var(--ink);
  }
  .performers {
    position: absolute;
    top: 592px;
    left: 110px;
    width: 630px;
    display: flex;
    justify-content: space-between;
  }
  .performer {
    width: 190px;
    text-align: center;
  }
  .performer-photo {
    width: 128px;
    height: 128px;
    margin: 0 auto 12px;
    background: linear-gradient(180deg, #8e857a 0%, #4d4741 100%);
  }
  .performer-name {
    margin: 0;
    font-family: "Oswald", Impact, sans-serif;
    font-weight: 600;
    font-size: 20px;
    letter-spacing: 0.5px;
    text-transform: uppercase;
  }
  .performer-role {
    margin: 0;
    font-family: "Oswald", Impact, sans-serif;
    font-weight: 400;
    font-size: 13px;
    letter-spacing: 1px;
    text-transform: uppercase;
    color: var(--ink-soft);
  }
  .cast-note {
    position: absolute;
    left: 0; right: 0;
    top: 808px;
    margin: 0;
    text-align: center;
    font-family: "Oswald", Impact, sans-serif;
    font-weight: 600;
    font-size: 22px;
    letter-spacing: 1px;
  }
  .details-label {
    position: absolute;
    left: 0; right: 0;
    top: 852px;
    margin: 0;
    text-align: center;
    font-family: "Oswald", Impact, sans-serif;
    font-size: 12px;
    letter-spacing: 1.5px;
    color: var(--ink-soft);
  }
  .event-date {
    position: absolute;
    left: 0; right: 0;
    top: 866px;
    margin: 0;
    text-align: center;
    font-family: "Oswald", Impact, sans-serif;
    font-weight: 700;
    font-size: 46px;
    letter-spacing: 1px;
  }
  .event-venue {
    position: absolute;
    left: 0; right: 0;
    top: 930px;
    margin: 0;
    text-align: center;
    font-family: "Oswald", Impact, sans-serif;
    font-weight: 500;
    font-size: 17px;
    letter-spacing: 0.8px;
    text-transform: uppercase;
  }
  .divider {
    position: absolute;
    left: 150px;
    top: 972px;
    width: 549px;
    height: 1px;
    background: var(--ink-faint);
  }
  .seating-note {
    position: absolute;
    left: 0; right: 0;
    top: 986px;
    margin: 0;
    text-align: center;
    font-family: "Oswald", Impact, sans-serif;
    font-size: 12px;
    letter-spacing: 1.5px;
    color: var(--ink-soft);
  }
  .ticket-line {
    position: absolute;
    left: 0; right: 0;
    top: 1002px;
    margin: 0;
    text-align: center;
    font-family: "Oswald", Impact, sans-serif;
    font-weight: 700;
    font-size: 33px;
    letter-spacing: 0.5px;
  }
</style>
</head>
<body>
<main class="poster">
  <div class="backdrop-texture"></div>

  <div class="hero-portrait" role="img" aria-label="Portrait photograph of the honored composer beside a sculpted figure"></div>
  <h1 class="event-title">VELARDO</h1>

  <h2 class="tagline">TRIBUTE TO THE PRINCE OF SAMBA LENTA</h2>

  <p class="description">Experience a vibrant 90-minute musical tribute to the legendary Aurélio Campos Velardo – the man who brought Samba Lenta to the world. This immersive show blends live music, rich narration, and captivating multimedia to bring Velardo's story to life. From iconic melodies to behind-the-music moments, you'll feel the heartbeat of Brazil in a celebration that honors the genius, the legacy, and the unmistakable rhythm of Samba Lenta.</p>

  <section class="performers">
    <div class="performer">
      <div class="performer-photo" role="img" aria-label="Photo of Gus Pemberly"></div>
      <p class="performer-name">Gus Pemberly</p>
      <p class="performer-role">Music Director</p>
    </div>
    <div class="performer">
      <div class="performer-photo" role="img" aria-label="Photo of Ida Lusk"></div>
      <p class="performer-name">Ida Lusk</p>
      <p class="performer-role">Vocalist</p>
    </div>
    <div class="performer">
      <div class="performer-photo" role="img" aria-label="Photo of Neil Soward"></div>
      <p class="performer-name">Neil Soward</p>
      <p class="performer-role">Emcee</p>
    </div>
  </section>

  <p class="cast-note">…AND A CAST OF PROFESSIONAL MUSICIANS.</p>

  <p class="details-label">EVENT TIME AND LOCATION</p>
  <p class="event-date">SUNDAY, MAY 17 &nbsp;3:00 - 5:00PM</p>
  <p class="event-venue">Lark Hollow Auditorium &nbsp;2716 W 8th Ct, Tulsa, OK 74125, USA</p>

  <div class="divider"></div>

  <p class="seating-note">ALL SEATS RESERVED</p>
  <p class="ticket-line">TICKETS AVAILABLE AT LARKHOLLOWSTAGE.COM</p>
</main>
</body>
</html>
```